Zielgruppe
Friseurin für Damen und Herren
Aufgabenstellung
https://lumiraschnitt.de
Bitte erstelle mir anhand der Daten von der Website einen angepassten Entwurf mit Neueröffnung und geben keine Preise an sondern die kunden sollen sich direkt eingeladen führen um persönlich vor Ort vorbei zuschauen.

```html
<!DOCTYPE html>
<html lang="de">
<head>
<meta charset="utf-8">
<title>Lumira Hair &amp; Beautylounge – Neueröffnung</title>
<link rel="stylesheet" href="https://fonts.googleapis.com/css2?family=Bodoni+Moda:wght@500&family=Montserrat:ital,wght@0,400;0,600;1,400&display=swap">
<style>
  :root {
    --sage: #67775a;
    --white: #ffffff;
    --ink: #141414;
    --logo-ink: #1f2a2a;
    --rose: #e6c3b8;
    --gold-1: #c9971c;
    --gold-2: #f0c53a;
    --gold-3: #d9a824;
    --hair-1: #e8d7c4;
    --hair-2: #b9774d;
    --hair-3: #8a4a2a;
    --hair-4: #c98a5a;
  }
  html, body { margin: 0; padding: 0; overflow: hidden; }
  body { width: 1200px; height: 851px; background: var(--sage); }
  .flyer {
    position: relative; width: 1200px; height: 851px; overflow: hidden;
    background: var(--sage); font-family: "Montserrat", sans-serif; color: var(--white);
  }
  .flyer__shapes { position: absolute; inset: 0; }
  .brand-box {
    position: absolute; left: 180px; top: 0; width: 377px; height: 194px;
    background: var(--white); display: flex; flex-direction: column;
    align-items: center; justify-content: center; gap: 10px;
    color: var(--logo-ink); font-family: "Montserrat", sans-serif; font-weight: 400;
  }
  .brand-box__name { font-size: 56px; letter-spacing: 2px; line-height: 1; }
  .brand-box__sub { font-size: 25px; letter-spacing: -0.5px; line-height: 1; }
  .headline {
    position: absolute; left: 72px; top: 262px; margin: 0;
    font-family: "Bodoni Moda", serif; font-weight: 500; font-size: 78px;
    color: var(--ink); letter-spacing: -1px; line-height: 1;
  }
  .copy {
    position: absolute; left: 70px; width: 560px; margin: 0;
    text-align: center; text-transform: uppercase; font-size: 16.5px; line-height: 29px;
  }
  .copy--intro { top: 430px; }
  .copy--invite { top: 565px; }
  .copy--invite strong { color: var(--rose); font-weight: 600; }
  .copy--call { top: 646px; font-style: italic; line-height: 28px; }
</style>
</head>
<body>
<main class="flyer">
  <svg class="flyer__shapes" width="1200" height="851" viewBox="0 0 1200 851">
    <defs>
      <linearGradient id="hairTone" x1="0" y1="0" x2="1" y2="1">
        <stop offset="0" stop-color="var(--hair-2)"/>
        <stop offset="0.35" stop-color="var(--hair-3)"/>
        <stop offset="0.6" stop-color="var(--hair-4)"/>
        <stop offset="1" stop-color="var(--hair-1)"/>
      </linearGradient>
      <linearGradient id="goldTone" x1="0" y1="0" x2="1" y2="1">
        <stop offset="0" stop-color="var(--gold-1)"/>
        <stop offset="0.5" stop-color="var(--gold-2)"/>
        <stop offset="1" stop-color="var(--gold-3)"/>
      </linearGradient>
      <linearGradient id="glassTone" x1="0" y1="0" x2="0" y2="1">
        <stop offset="0" stop-color="#e9dc8a" stop-opacity="0.45"/>
        <stop offset="0.5" stop-color="#d8c46a" stop-opacity="0.3"/>
        <stop offset="1" stop-color="#ffffff" stop-opacity="0.08"/>
      </linearGradient>
    </defs>
    <polygon points="706,0 1200,0 1200,851 600,851" fill="url(#hairTone)"
             role="img" aria-label="Foto: lange, rotblonde Locken"/>
    <rect x="24" y="440" width="211" height="411" rx="30" fill="url(#glassTone)"
          role="img" aria-label="Foto: zwei anstoßende Sektgläser"/>
    <rect x="56.5" y="59.5" width="1114" height="744" fill="none" stroke="var(--white)" stroke-width="1.6"/>
    <rect x="0" y="227" width="794" height="154" fill="url(#goldTone)"/>
  </svg>

  <div class="brand-box">
    <span class="brand-box__name">LUMIRA</span>
    <span class="brand-box__sub">HAIR &amp; BEAUTYLOUNGE</span>
  </div>

  <h1 class="headline">NEUERÖFFNUNG</h1>

  <p class="copy copy--intro">Schönheit und Stil in perfekter Harmonie –<br>dein neuer Friseursalon in Grünhaiting<br>für Damen &amp; Herren .</p>
  <p class="copy copy--invite">Wir laden dich herzlich zur Neueröffnung<br>der <strong>Lumira Hair &amp; Beautylounge</strong> ein.</p>
  <p class="copy copy--call">Komm vorbei, lerne uns kennen<br>und entdecke deinen neuen Lieblingsplatz<br>für Haare &amp; Beauty.</p>
</main>
</body>
</html>
```